Pharmacy Retail eCommerce Site Design

NOTE: THIS IS AN eCommerce Design contest NOT logo Design

Our client Marwen Pharmacy is the largest pharmacy chain in the country of Qatar. we developed the eCommerce site for them with advance features including AI/Machine learning capabilities
We are looking for eCommerce graphic design experts ( preferably with experience designing for pharmacy chains) to take the pages we built, redesign the graphics of each page.
We are open to ideas to change user navigations based on the contestant past experience designing eCommerce site

THE OUTCOME OF THE COMPETITION:
1) provide 2graphic designs for each page on the current site ( link is provided below). One design is a dark theme and the other is a light theme design. for our client executives to select one

to view the eCommerce site under development please visit the following link . ( https://marwen-pharmacy.stagevaultix.com/)

Attached you will see the logo of the pharmacy chain, to be used as a guidance for the colour pallet of the design

additionally you visit the pharmacy website to gain better idea of their values , https://www.marwen-pharmacy.com/

The design needs to be stunning and better than their main competitors in Qatar
Here is the main competitor eCommerce site
https://www.dawatrixcare.qa/

```html
<!DOCTYPE html>
<html lang="en">
<head>
<meta charset="utf-8">
<title>Marwen Pharmacy</title>
<link href="https://fonts.googleapis.com/css2?family=Poppins:wght@400;500;600;700&display=swap" rel="stylesheet">
<style>
:root{
  --green:#5aad2f;
  --red:#c0282d;
  --ink:#222;
  --muted:#777;
  --line:#e4e4e4;
  --teal-a:#2c7f86;
  --teal-b:#3fa99b;
  --gray-band:#e9e9e9;
}
*{box-sizing:border-box;margin:0;padding:0}
html,body{width:1200px;height:3124px;overflow:hidden}
body{font-family:"Poppins",sans-serif;color:var(--ink);background:#fff;position:relative}
.wrap{width:1008px;margin:0 auto}
svg{display:block}

.topbar{height:27px;background:var(--green);color:#fff;font-size:10px;font-weight:500}
.topbar .wrap{display:flex;align-items:center;height:100%;gap:14px}
.topbar .item{display:flex;align-items:center;gap:8px}
.topbar .sep{width:1px;height:17px;background:rgba(255,255,255,.6);margin:0 12px}
.topbar .right{margin-left:auto;display:flex;gap:18px;align-items:center;opacity:.85}

.header{height:74px;border-bottom:1px solid var(--line)}
.header .wrap{display:flex;align-items:center;height:100%}
.brand{display:flex;align-items:center;gap:6px;font-weight:700;color:var(--red);font-size:13px;width:152px;flex-shrink:0;white-space:nowrap}
.brand i{width:14px;height:14px;background:var(--green);border-radius:50%;flex-shrink:0}
.nav{display:flex;gap:15px;font-size:10.5px;text-transform:uppercase;font-weight:500;white-space:nowrap}
.nav a{color:#333;text-decoration:none}
.nav a.active{color:var(--green)}
.header .tools{margin-left:auto;display:flex;gap:16px}

.hero{height:394px;background:linear-gradient(90deg,#3d3d3d,#5a5a5a 55%,#4a4a4a);color:#fff;text-align:center;padding-top:134px}
.hero h1{font-size:20px;font-weight:600;letter-spacing:.3px}
.hero p{font-size:10.5px;width:360px;margin:18px auto 0;line-height:1.45;opacity:.9}
.btn-white{display:inline-block;background:#fff;color:#222;font-size:10px;font-weight:600;padding:7px 18px;margin-top:34px;text-transform:uppercase}

.promos{display:flex;gap:16px;margin-top:42px}
.promo{flex:1;height:282px;background:linear-gradient(120deg,var(--teal-a),var(--teal-b));display:flex;align-items:center;padding:0 30px;color:#fff;position:relative}
.promo h3{font-size:14px;font-weight:600;text-transform:uppercase}
.promo .price{font-size:17px;font-weight:600;margin-top:14px}
.promo .btn-white{margin-top:42px;font-size:10px;padding:7px 20px}
.promo .art{position:absolute;right:30px;top:38px;width:150px;height:200px;border-radius:10px;background:linear-gradient(#e9f1ef,#cfe0dd)}

.tabs{display:flex;gap:30px;margin-top:40px;font-size:11.5px;font-weight:500;text-transform:uppercase}
.tabs .on{color:var(--red);border-bottom:2px solid var(--red);padding-bottom:5px}

.grid{display:flex;gap:5px;margin-top:50px}
.cells{width:722px;display:grid;grid-template-columns:repeat(4,177px);grid-template-rows:186px 187px;row-gap:37px;column-gap:4px}
.cell{background:#f3f3f3;border:1px solid #ececec;text-align:center;position:relative;padding-top:20px}
.cell .pic{width:40px;height:78px;margin:0 auto;border-radius:5px;background:linear-gradient(#dfe6ee,#b9c6d6)}
.cell .name{font-size:9px;text-transform:uppercase;color:#444;margin:12px 18px 0;line-height:1.4;height:26px}
.cell .pr{font-size:14px;font-weight:600;margin-top:10px}
.red{color:var(--red)}
.tag{position:absolute;top:8px;left:10px;font-size:7px;color:#fff;padding:1px 5px;font-weight:600}
.tag.new{background:var(--green)}.tag.sale{background:var(--red)}
.cell.hover{background:#6d6d6d}
.cell.hover .pic{opacity:.35}
.qv{position:absolute;left:40px;top:84px;background:#fff;font-size:10px;padding:3px 8px;color:#666}
.hover-icons{position:absolute;bottom:20px;left:0;right:0;display:flex;justify-content:center;gap:22px}
.feature{width:287px;height:410px;border:1px solid #ececec;text-align:center;padding-top:20px}
.feature .pic{width:118px;height:178px;margin:0 auto;border-radius:14px;background:linear-gradient(#f4f4f4,#1c3f8f 70%)}
.feature .name{font-size:9px;font-weight:500;text-transform:uppercase;margin:34px 30px 0;line-height:1.5}
.feature .pr{font-size:15px;font-weight:600;color:var(--red);margin-top:16px}
.timer{display:flex;justify-content:center;gap:8px;margin-top:22px}
.timer div{width:42px}
.timer small{font-size:8px;font-weight:600;display:block}
.timer b{display:block;background:var(--green);color:#fff;font-size:15px;padding:4px 0;margin-top:5px}

.cats{background:var(--gray-band);height:479px;padding-top:44px;position:relative}
.sec-title{text-align:center;font-size:17px;font-weight:600;text-transform:uppercase}
.cat-row{display:flex;gap:6px;margin-top:37px}
.cat{width:247px;height:280px;background:#fff}
.cat .pic{height:145px;background:linear-gradient(135deg,#c9b7a6,#8c9aa8)}
.cat h4{font-size:12px;font-weight:600;text-transform:uppercase;margin:24px 12px 0}
.cat p{font-size:9.5px;color:var(--muted);margin:6px 12px 0;line-height:1.45}
.btn-out{display:inline-block;border:1px solid var(--red);color:#222;font-size:10px;font-weight:600;padding:4px 17px;margin:12px 12px 0}
.arrow{position:absolute;top:300px}

.offers{padding-top:52px}
.offer-grid{display:grid;grid-template-columns:repeat(5,187px);column-gap:18px;row-gap:35px;margin-top:37px}
.offer{height:238px;border:1px solid var(--line);text-align:center;padding-top:24px}
.offer .pic{width:52px;height:72px;margin:0 auto;border-radius:5px;background:linear-gradient(#e6ecef,#8ea7b6)}
.offer .name{font-size:9px;text-transform:uppercase;color:#444;margin:22px 16px 0;line-height:1.45;height:28px}
.offer .pr{font-size:15px;font-weight:600;margin-top:10px}
.offer .btn-out{margin:12px 0 0}

.brands{padding-top:50px}
.brand-row{display:flex;gap:8px;margin-top:34px}
.brand-box{width:162px;height:64px;box-shadow:0 1px 4px rgba(0,0,0,.15);display:flex;align-items:center;justify-content:center;font-size:11px;color:#999;letter-spacing:1px;font-weight:500}

.support{height:156px;background:var(--green);margin-top:46px;color:#fff}
.support .wrap{display:flex;align-items:center;height:100%}
.support .msg{display:flex;gap:16px;align-items:center;font-size:14px;font-weight:500;text-transform:uppercase;line-height:1.4;width:440px}
.support .news{display:flex;gap:16px;align-items:center;font-size:14px;font-weight:600;text-transform:uppercase;line-height:1.3;width:212px}
.sub{display:flex;height:34px}
.sub .field{width:236px;background:#fff;display:flex;align-items:center;gap:8px;padding-left:12px;color:#bbb;font-size:11px}
.sub .go{background:var(--red);color:#fff;font-size:13px;font-weight:600;padding:0 12px;display:flex;align-items:center}

.footer .wrap{display:flex;padding-top:42px}
.fcol h5{font-size:14px;font-weight:600;margin-bottom:10px}
.fcol li{list-style:none;font-size:9.5px;color:#444;line-height:19px}
.contact li{display:flex;gap:12px;align-items:center;line-height:21px}
.copy{position:absolute;left:95px;top:3012px;font-size:9px;color:#999}
</style>
</head>
<body>

<div class="topbar"><div class="wrap">
  <span class="item"><svg width="13" height="10" viewBox="0 0 13 10"><rect x=".5" y=".5" width="12" height="9" fill="none" stroke="#fff"/><path d="M.5 .5l6 5 6-5" fill="none" stroke="#fff"/></svg>hello@marwenpharmacy.qa</span>
  <span class="sep"></span>
  <span class="item"><svg width="10" height="10" viewBox="0 0 10 10"><path d="M2 0l2 2.5-1 1.5c.6 1.4 1.6 2.4 3 3l1.5-1L10 8 8.5 10C4 9.5.5 6 0 1.5z" fill="#fff"/></svg>(974) 555-0142</span>
  <span class="right"><span>USD ⌄</span><span>English ⌄</span><svg width="11" height="12" viewBox="0 0 11 12"><circle cx="5.5" cy="3.5" r="3" fill="none" stroke="#fff"/><path d="M.5 12c0-3 2.2-5 5-5s5 2 5 5" fill="none" stroke="#fff"/></svg></span>
</div></div>

<header class="header"><div class="wrap">
  <div class="brand"><i></i>Marwen Pharmacy</div>
  <nav class="nav">
    <a class="active">Medicines</a><a>Supplements</a><a>Beautycare</a><a>Junior Products</a><a>Health Care Products</a><a>Personal Care</a><a>Medical Devices</a>
  </nav>
  <div class="tools">
    <svg width="15" height="13" viewBox="0 0 15 13"><path d="M7.5 12S1 8 1 4a3 3 0 016.5-1A3 3 0 0114 4c0 4-6.5 8-6.5 8z" fill="none" stroke="#999"/></svg>
    <svg width="17" height="14" viewBox="0 0 17 14"><path d="M0 1h3l2 8h9l2-6H4" fill="none" stroke="var(--green)" stroke-width="1.4"/><circle cx="6" cy="12" r="1.3" fill="var(--green)"/><circle cx="13" cy="12" r="1.3" fill="var(--green)"/><circle cx="15" cy="1.5" r="1.8" fill="var(--red)"/></svg>
    <svg width="14" height="14" viewBox="0 0 14 14"><circle cx="6" cy="6" r="5" fill="none" stroke="#999" stroke-width="1.3"/><path d="M10 10l3.5 3.5" stroke="#999" stroke-width="1.3"/></svg>
  </div>
</div></header>

<section class="hero" role="img" aria-label="Pharmacist holding a tablet in front of pharmacy shelves">
  <h1>PRECISE AND DEPENDABLE PHARMACIST</h1>
  <p>Lorem ipsum dolor sit amet, consectetur adipiscing elit, sed do eiusmod tempor incididunt ut labore et dolore magna aliqua.</p>
  <span class="btn-white">Shop Now</span>
</section>

<div class="wrap">
  <div class="promos">
    <div class="promo"><div><h3>Herbora Hepa 48 Tab 100's</h3><div class="price">24.25 QR</div><span class="btn-white">Shop Now</span></div><div class="art" role="img" aria-label="Herbal tablet bottle and box"></div></div>
    <div class="promo"><div><h3>Sweetora Stevia Sweet 75G X</h3><div class="price">34.00 QR</div><span class="btn-white">Shop Now</span></div><div class="art" role="img" aria-label="Stevia sweetener jar" style="width:100px;right:50px"></div></div>
  </div>

  <div class="tabs"><span class="on">New Arrivals</span><span>Sale Products</span><span>Hots Products</span></div>

  <div class="grid">
    <div class="cells">
      <div class="cell"><div class="pic" role="img" aria-label="Facial cream tube"></div><div class="name">Daily Revitalizing Facial Cream 60ml X</div><div class="pr">89 QR</div></div>
      <div class="cell"><div class="pic" role="img" aria-label="Cleansing gel bottle"></div><div class="name">Mirabel 2 in 1 Hair &amp; Body Cleansing Gel 200ml</div><div class="pr red">44 QR</div></div>
      <div class="cell"><span class="tag new">NEW</span><div class="pic" role="img" aria-label="Green cleansing foam bottle" style="background:linear-gradient(#bfe58f,#4caa2a)"></div><div class="name">Lumerac Pure Foaming Cleanser 200ml* XXX</div><div class="pr">128 QR</div></div>
      <div class="cell"><div class="pic" role="img" aria-label="Bronze body spray bottle" style="background:linear-gradient(#e6c09a,#a9653a)"></div><div class="name">Floraine Sun Glow Body 50 - 150ml</div><div class="pr">178 QR</div></div>
      <div class="cell"><div class="pic" role="img" aria-label="Perfume box and bottle" style="width:66px;background:linear-gradient(#a11a24,#3a0a0e)"></div><div class="name">Encora Velvet Night EDP 30ml</div><div class="pr">59 QR</div></div>
      <div class="cell"><span class="tag sale">SALE</span><div class="pic" role="img" aria-label="Nasal spray box and bottle" style="width:56px"></div><div class="name">Marisal Nose Care Ent 200ml</div><div class="pr red">49 QR</div></div>
      <div class="cell hover"><div class="pic" role="img" aria-label="Skincare products"></div><span class="qv">◉ Quick View</span><div class="hover-icons"><svg width="14" height="12" viewBox="0 0 15 13"><path d="M7.5 12S1 8 1 4a3 3 0 016.5-1A3 3 0 0114 4c0 4-6.5 8-6.5 8z" fill="none" stroke="#fff"/></svg><svg width="15" height="12" viewBox="0 0 17 14"><path d="M0 1h3l2 8h9l2-6H4" fill="none" stroke="#fff" stroke-width="1.4"/><circle cx="6" cy="12" r="1.3" fill="#fff"/><circle cx="13" cy="12" r="1.3" fill="#fff"/></svg></div></div>
      <div class="cell"><div class="pic" role="img" aria-label="Serum boxes and bottle" style="width:56px;background:linear-gradient(#e6eaf4,#2e3f9e)"></div><div class="name">Novastra Firming Renewal Serum 30ml</div><div class="pr">359 QR</div></div>
    </div>
    <div class="feature">
      <div class="pic" role="img" aria-label="Hair, skin and nails supplement bottle"></div>
      <div class="name">Vitagen Hair,Skin &amp; Nails Cap 60's *Cancelled Registration</div>
      <div class="pr">62.65 QR</div>
      <div class="timer"><div><small>DAYS</small><b>02</b></div><div><small>HOURS</small><b>04</b></div><div><small>MIN</small><b>02</b></div><div><small>SEC</small><b>00</b></div></div>
    </div>
  </div>
</div>

<section class="cats">
  <div class="sec-title">Shop By Category</div>
  <svg class="arrow" style="left:38px" width="14" height="26" viewBox="0 0 14 26"><path d="M12 1L2 13l10 12" fill="none" stroke="#bbb" stroke-width="1.5"/></svg>
  <svg class="arrow" style="right:38px" width="14" height="26" viewBox="0 0 14 26"><path d="M2 1l10 12L2 25" fill="none" stroke="#bbb" stroke-width="1.5"/></svg>
  <div class="wrap cat-row">
    <div class="cat"><div class="pic" role="img" aria-label="Assorted colourful pills and capsules"></div><h4>Medicines</h4><p>Lorem ipsum dolor sit amet elit, sed do eiusmod tempor incididunt</p><span class="btn-out">Show More</span></div>
    <div class="cat"><div class="pic" role="img" aria-label="Sport nutrition tubs" style="background:linear-gradient(135deg,#e8e8e8,#9a9a9a)"></div><h4>Supplements</h4><p>Lorem ipsum dolor sit amet elit, sed do eiusmod tempor incididunt</p><span class="btn-out">Show More</span></div>
    <div class="cat"><div class="pic" role="img" aria-label="Face cream jar and box" style="background:linear-gradient(135deg,#f7f2ea,#c7a77d)"></div><h4>Beauty Care</h4><p>Lorem ipsum dolor sit amet elit, sed do eiusmod tempor incididunt</p><span class="btn-out">Show More</span></div>
    <div class="cat"><div class="pic" role="img" aria-label="Assorted colourful pills and capsules"></div><h4>Personal Care</h4><p>Lorem ipsum dolor sit amet elit, sed do eiusmod tempor incididunt</p><span class="btn-out">Show More</span></div>
  </div>
</section>

<section class="offers wrap">
  <div class="sec-title">Top Offers</div>
  <div class="offer-grid">
    <div class="offer"><div class="pic" role="img" aria-label="Perfume gift box"></div><div class="name">Encora Velvet Night EDP 30ml</div><div class="pr">279 QR</div><span class="btn-out">Add to Cart</span></div>
    <div class="offer"><div class="pic" role="img" aria-label="Cleansing foam bottle" style="width:30px;background:linear-gradient(#dff4ee,#3fb29a)"></div><div class="name">Lumerac Pure Foaming Cleanser 200ml* XXX</div><div class="pr red">128 QR</div><span class="btn-out">Add to Cart</span></div>
    <div class="offer"><div class="pic" role="img" aria-label="Cream box and tube"></div><div class="name">Encora Velvet Night EDP 30ml</div><div class="pr">279 QR</div><span class="btn-out">Add to Cart</span></div>
    <div class="offer"><div class="pic" role="img" aria-label="Omega supplement bottle" style="background:linear-gradient(#f0f0f0,#6b4fa1)"></div><div class="name">Nutriwell Omega 3-6-9 1200mg SGC 90's (NW3335)</div><div class="pr">93.50 QR</div><span class="btn-out">Add to Cart</span></div>
    <div class="offer"><div class="pic" role="img" aria-label="Syrup box and bottle" style="background:linear-gradient(#3d7ba8,#7a2a14)"></div><div class="name">Herbora Respira Syrup 200ml</div><div class="pr">30.50QR</div><span class="btn-out">Add to Cart</span></div>
    <div class="offer"><div class="pic" role="img" aria-label="Sunscreen cream bottle" style="width:30px"></div><div class="name">Skin Whitening Cream W/Sunscreen 60ml</div><div class="pr">98.00 QR</div><span class="btn-out">Add to Cart</span></div>
    <div class="offer"><div class="pic" role="img" aria-label="Cream bottle" style="width:30px;background:linear-gradient(#f4f4f8,#c6cad8)"></div><div class="name">Anti Wrinkle Cream 10 AHA 120 ml</div><div class="pr red">99.00 QR</div><span class="btn-out">Add to Cart</span></div>
    <div class="offer"><div class="pic" role="img" aria-label="Baby scissors" style="width:30px;background:linear-gradient(#e3ebf7,#3a67b5)"></div><div class="name">Corvy Baby Scissors Stain-less Pink #1030PI</div><div class="pr">104.00 QR</div><span class="btn-out">Add to Cart</span></div>
    <div class="offer"><div class="pic" role="img" aria-label="Slanted tweezers" style="width:24px;background:linear-gradient(#eee,#555)"></div><div class="name">Tweezers Small Slanted @ 1067</div><div class="pr">9.50 QR</div><span class="btn-out">Add to Cart</span></div>
    <div class="offer"><div class="pic" role="img" aria-label="Nail nipper" style="width:60px;background:linear-gradient(135deg,#f4f4f4,#9a9a9a)"></div><div class="name">Nail Nipper With Spring 14CM@-1080</div><div class="pr">84.00QR</div><span class="btn-out">Add to Cart</span></div>
  </div>
</section>

<section class="brands wrap">
  <div class="sec-title">Top Brands</div>
  <div class="brand-row">
    <div class="brand-box">PHARMACY STORE</div><div class="brand-box">PHARMACY</div><div class="brand-box">HERBAL HEART</div>
    <div class="brand-box">PHARMACY STORE</div><div class="brand-box">PHARMACY</div><div class="brand-box">HERBAL HEART</div>
  </div>
</section>

<section class="support"><div class="wrap">
  <div class="msg"><svg width="26" height="30" viewBox="0 0 26 30"><circle cx="13" cy="10" r="6" fill="#fff"/><path d="M3 12a10 10 0 0120 0" fill="none" stroke="#fff" stroke-width="2"/><path d="M2 30c0-7 5-11 11-11s11 4 11 11z" fill="#fff"/></svg><span>We offer 24/7 dedicated support<br>If you need support send us a message</span></div>
  <div class="news"><svg width="30" height="26" viewBox="0 0 30 26"><path d="M0 11L30 0 23 26 14 17z" fill="#fff"/><path d="M14 17L30 0" stroke="var(--green)" stroke-width="1.5"/></svg><span>Subscribe our<br>newsletter</span></div>
  <div class="sub"><div class="field"><svg width="13" height="10" viewBox="0 0 13 10"><rect x=".5" y=".5" width="12" height="9" fill="none" stroke="#bbb"/><path d="M.5 .5l6 5 6-5" fill="none" stroke="#bbb"/></svg>EMAIL</div><div class="go">SUBSCRIBE</div></div>
</div></section>

<footer class="footer"><div class="wrap">
  <div class="fcol" style="width:280px"><h5>Quick Links</h5><ul><li>About Us</li><li>Shipping &amp; Returns</li><li>Privacy Policy</li><li>Terms &amp; Conditions</li><li>Vacancies</li></ul></div>
  <div class="fcol" style="width:260px;padding-top:4px"><h5>Accounts</h5><ul><li>Wishlist</li><li>Compare</li><li>Log In</li><li>Subscribe</li></ul></div>
  <div class="fcol" style="width:274px"><h5>Categories</h5><ul><li>Medicines</li><li>supplements</li><li>beauty care</li><li>junior products</li><li>Health care products</li><li>Personal Care</li><li>Medical Devices</li></ul></div>
  <div class="fcol contact"><h5>Contact Us</h5><ul>
    <li><svg width="13" height="10" viewBox="0 0 13 10"><rect x=".5" y=".5" width="12" height="9" fill="none" stroke="#333"/><path d="M.5 .5l6 5 6-5" fill="none" stroke="#333"/></svg>hello@marwenpharmacy.qa</li>
    <li><svg width="11" height="11" viewBox="0 0 10 10"><path d="M2 0l2 2.5-1 1.5c.6 1.4 1.6 2.4 3 3l1.5-1L10 8 8.5 10C4 9.5.5 6 0 1.5z" fill="#333"/></svg>(974) 555-0142</li>
  </ul></div>
</div>
<div class="copy">copyright@marwenpharmacy.com. ALL RIGHTS RESERVED</div>
</footer>

</body>
</html>
```